Casa Vero Inspections Business Card

I need a business card for my new company. The company is going to provide home inspections. The name of the company is Casa Vero Inspections. I am not sure if I want a single sided card or a double. I have a logo already that I want to incorporate into the card design. I was wondering if I should incorporate a catch phrase on my card or not. If I did the phrase would be "Clear Answers for Every Home You Buy" but i am unsure how or if to use it on a card. The following information needs to be on the card.
Home Inspection
My Name: Marcus T. Wolford Phone Number: 555-301-7762 Email: mwolford@casaveroinspections.com Website: www.casaveroinspections.com NY HI License # 27300519462

```html
<!DOCTYPE html>
<html lang="en">
<head>
<meta charset="utf-8">
<title>Casa Vero Inspections Business Card</title>
<link href="https://fonts.googleapis.com/css2?family=Montserrat:wght@500;600;700&display=swap" rel="stylesheet">
<style>
  :root {
    --backdrop: #6a6a6a;
    --card: #ffffff;
    --brand: #0b65a3;
    --brand-dark: #004f80;
    --brand-light: #7cc3ee;
  }
  * { margin: 0; padding: 0; box-sizing: border-box; }
  html, body {
    width: 1199px; height: 1200px; overflow: hidden;
    background: var(--backdrop);
    font-family: "Montserrat", sans-serif;
    color: var(--brand);
  }
  .card {
    position: absolute; left: 202px; width: 796px; height: 442px;
    background: var(--card);
  }
  .card--front { top: 117px; }
  .card--back { top: 616px; }

  .brand-name {
    position: absolute; left: 93px; top: 182px;
    display: flex; align-items: center; gap: 12px;
    font-weight: 700; font-size: 30px; line-height: 1.1;
    color: var(--brand);
  }
  .brand-name__mark {
    width: 22px; height: 22px; background: var(--brand); flex: none;
  }
  .tagline {
    position: absolute; left: 406px; top: 168px;
    font-weight: 500; font-size: 31px; line-height: 38px;
    letter-spacing: 0.5px;
  }

  .holder {
    position: absolute; left: 66px; top: 115px;
    font-weight: 700; font-size: 37px; letter-spacing: 0.3px;
  }
  .contacts { position: absolute; left: 68px; top: 184px; list-style: none; }
  .contacts li {
    display: flex; align-items: center; gap: 15px;
    height: 33px; margin-bottom: 8px;
    font-weight: 600; font-size: 23px;
  }
  .contacts__icon {
    width: 33px; height: 33px; background: var(--brand);
    display: flex; align-items: center; justify-content: center; flex: none;
  }
  .contacts__icon svg { width: 20px; height: 20px; }
  .license {
    position: absolute; left: 67px; top: 316px;
    font-weight: 600; font-size: 22px;
  }
</style>
</head>
<body>
  <section class="card card--front">
    <div class="brand-name"><span class="brand-name__mark"></span><span>Casa Vero<br>Inspections</span></div>
    <p class="tagline">Clear Answers<br>for Every Home<br>You Buy</p>
  </section>

  <section class="card card--back">
    <h1 class="holder">Marcus T. Wolford</h1>
    <ul class="contacts">
      <li>
        <span class="contacts__icon">
          <svg viewBox="0 0 24 24"><path fill="#fff" d="M6.6 10.8a15.1 15.1 0 0 0 6.6 6.6l2.2-2.2c.3-.3.7-.4 1-.2 1.1.4 2.3.6 3.6.6.6 0 1 .4 1 1V20c0 .6-.4 1-1 1A17 17 0 0 1 3 4c0-.6.4-1 1-1h3.5c.6 0 1 .4 1 1 0 1.3.2 2.5.6 3.6.1.3 0 .7-.2 1z"/></svg>
        </span>555-301-7762
      </li>
      <li>
        <span class="contacts__icon">
          <svg viewBox="0 0 24 24" fill="none" stroke="#fff" stroke-width="1.8"><rect x="3" y="5" width="18" height="14"/><path d="M3 5l9 8 9-8M3 19l7-7M21 19l-7-7"/></svg>
        </span>mwolford@casaveroinspections.com
      </li>
      <li>
        <span class="contacts__icon">
          <svg viewBox="0 0 24 24" fill="none" stroke="#fff" stroke-width="1.6"><circle cx="12" cy="12" r="9"/><ellipse cx="12" cy="12" rx="4" ry="9"/><path d="M3 12h18M5 7h14M5 17h14"/></svg>
        </span>casaveroinspections.com
      </li>
    </ul>
    <p class="license">NY HI License # 27300519462</p>
  </section>
</body>
</html>
```